Web page design/layout for dog breeder

We are looking for a new layout/design for our current web page. Current web pages can be found at http://ruddyhound.sitefold.com.

We recently uploaded the PTR Kennel of Renown banner that we would like to have displayed on the home page.

```html
<!DOCTYPE html>
<html lang="en">
<head>
<meta charset="utf-8">
<title>Ruddyhound Vizslas</title>
<link href="https://fonts.googleapis.com/css2?family=Open+Sans:wght@300;400;600;700&display=swap" rel="stylesheet">
<style>
:root{
  --brown-dark:#5a2f1c;
  --bar:#8c6833;
  --call:#5c3b22;
  --sand:#cbb08a;
  --cream:#f0e7dd;
  --text:#2e2a28;
  --white:#fff;
}
*{box-sizing:border-box;margin:0;padding:0}
html,body{width:1023px;height:1200px;overflow:hidden;background:#fff;font-family:"Open Sans",sans-serif;color:var(--text)}
.page{position:absolute;left:40px;top:0;width:941px;height:1161px;background:#fff;box-shadow:0 0 6px rgba(0,0,0,.25)}
.abs{position:absolute}
.brand{left:18px;top:44px;display:flex;align-items:center;gap:8px;font-size:20px;font-weight:700;color:#222;letter-spacing:.5px}
.brand-dot{width:12px;height:12px;border-radius:50%;background:#222}
.owner{right:90px;top:30px;text-align:right}
.owner-name{font-size:18px;color:var(--brown-dark)}
.owner-mail{font-size:12px;color:var(--brown-dark)}
.avatar{right:8px;top:10px;width:75px;height:75px;border-radius:50%;background:radial-gradient(circle at 50% 40%,#c9a07e,#6d7f92 70%,#3f4e5a)}
.nav{left:0;top:94px;width:941px;height:40px;background:var(--bar);display:flex;align-items:center}
.nav a{color:#fff;text-decoration:none;font-size:14px;margin-left:12px;margin-right:17px}
.call{right:0;top:0;width:226px;height:40px;background:var(--call);color:#fff;font-size:18px;display:flex;align-items:center;justify-content:center}
.hero{left:0;top:134px;width:941px;height:308px;background:linear-gradient(90deg,#5b2e18 0%,#6a3820 40%,#8b4b2c 65%,#7a3f24 100%)}
.hero h1{position:absolute;left:12px;top:30px;font-weight:300;color:#fff;font-size:60px;line-height:66px}
.hero h2{position:absolute;left:12px;top:92px;font-weight:300;color:#fff;font-size:36.5px}
.members{left:15px;top:178px;width:407px;height:110px;background:rgba(140,90,60,.45);padding:6px 6px}
.members h3{color:#fff;font-weight:600;font-size:23px;margin-bottom:6px}
.members ul{list-style:none;display:grid;grid-template-columns:205px 1fr;row-gap:11px}
.members li{color:#fff;font-weight:300;font-size:18px;line-height:25px;padding-left:2px}
.welcome-photo{left:12px;top:461px;width:165px;height:232px;background:linear-gradient(#4a4646,#a86a3c 50%,#e4e4e6)}
.welcome{left:188px;top:458px;width:508px}
.welcome h2{font-weight:400;font-size:25px;color:var(--brown-dark);margin-bottom:8px}
.welcome p{font-size:14px;line-height:24px;padding-left:3px;font-weight:300;color:var(--text)}
.welcome a{display:inline-block;margin-top:6px;padding-left:3px;font-size:13px;font-weight:600;color:var(--brown-dark);text-decoration:underline}
.quick{left:712px;top:459px;width:218px;height:234px;background:var(--sand);border:1px solid #a88e66;border-radius:8px;padding:4px 9px}
.quick h3{font-size:18px;font-weight:600;color:var(--brown-dark);margin-bottom:8px}
.field{background:#fbfaf7;border:1px solid #d8cdb8;height:31px;margin-bottom:10px;font-size:13px;font-style:italic;color:#8a8580;padding:5px 9px;font-weight:300}
.field.tall{height:60px}
.submit{position:absolute;right:11px;bottom:10px;width:86px;height:31px;background:var(--call);color:#fff;font-weight:600;font-size:14px;display:flex;align-items:center;justify-content:center;border-radius:2px}
.dogs{left:0;top:712px;width:941px;height:270px;background:var(--cream)}
.dogs h2{position:absolute;left:0;width:941px;top:16px;text-align:center;font-size:24px;font-weight:700;color:var(--brown-dark);text-decoration:underline}
.dog{position:absolute;top:76px;display:flex;gap:12px}
.dog-photo{width:175px;height:133px;border:3px solid #fff}
.dog-info h4{font-size:13px;font-weight:400;color:var(--brown-dark);margin-top:-2px;margin-bottom:1px;white-space:nowrap}
.dog-info p{font-size:13px;line-height:24px;font-weight:300;color:var(--text)}
.arrow{position:absolute;top:237px;width:21px;height:21px;background:#d6c39f;border:1px solid #a88e66}
.info{left:0;top:1017px;width:941px;text-align:center}
.info h3{font-size:19px;font-weight:600;color:var(--brown-dark)}
.info-row{display:flex;justify-content:center;gap:32px;margin-top:8px;font-size:19px;font-weight:700;color:var(--brown-dark)}
.info-row span{display:flex;align-items:center;gap:6px}
.footer{left:0;top:1117px;width:941px;height:44px;background:var(--bar);color:#fff;font-size:11px;display:flex;align-items:center;padding-left:14px}
.footer nav{margin-left:auto;display:flex;gap:23px;padding-right:10px}
</style>
</head>
<body>
<div class="page">
  <div class="abs brand"><span class="brand-dot"></span>Ruddyhound Vizslas</div>
  <div class="abs owner"><div class="owner-name">Dale Marsh</div><div class="owner-mail">ruddyhound@mailpost.net</div></div>
  <div class="abs avatar" role="img" aria-label="Portrait photo of the breeder"></div>

  <nav class="abs nav">
    <a>Home</a><a>Our Dogs</a><a>Upcoming Litter</a><a>Contact Us</a><a>Photo Gallery</a><a>Past Litters</a>
    <div class="abs call">Call Us 515-555-0147</div>
  </nav>

  <section class="abs hero" role="img" aria-label="Close-up photo of a vizsla puppy">
    <h1>We are dedicated to</h1>
    <h2>raising, training and breeding vizslas</h2>
    <div class="abs members">
      <h3>Proud Members of</h3>
      <ul><li>Red Pointer Society</li><li>Ozark Gundog Club</li><li>Prairie Vizsla League</li><li>Platte Valley Vizsla Club</li></ul>
    </div>
  </section>

  <div class="abs welcome-photo" role="img" aria-label="Vizsla sitting in the snow wearing a red collar"></div>
  <section class="abs welcome">
    <h2>Welcome to Ruddyhound Vizslas</h2>
    <p>We were introduced to our first vizsla on a hunting trip in the mid 1990s.&nbsp; We were impressed by this medium sized dog that had a superior nose and high-class hunting ability. And so it began, our first vizsla, Duke, joined our family in 1999.<br>Our vizslas have always been a part of our family and spend many hours each year in the field with us as our hunting companions.&nbsp; We participate in NFA hunt tests and field trials with our vizsla family.</p>
    <a>Read more...</a>
  </section>

  <aside class="abs quick">
    <h3>Quick Contact</h3>
    <div class="field">Full name</div>
    <div class="field">Email Address</div>
    <div class="field tall">Your message</div>
    <div class="submit">Submit</div>
  </aside>

  <section class="abs dogs">
    <h2>OUR DOGS</h2>
    <div class="dog" style="left:20px">
      <div class="dog-photo" role="img" aria-label="Vizsla puppy standing on a show table" style="background:linear-gradient(#8a8f96,#c58a55 55%,#d9d4cc)"></div>
      <div class="dog-info" style="width:255px"><h4>Ruddyhound's Prairie Ember JH (Maple)</h4><p>Reg #: RV31572208<br>Maple is out of our Hazel and Ridgeline Steadfast Ranger and exemplifies everything we were hoping for with this breeding.</p></div>
    </div>
    <div class="dog" style="left:480px">
      <div class="dog-photo" role="img" aria-label="Vizsla standing in a dry grass field" style="background:linear-gradient(#6d5a3e,#9c7a4e 55%,#b59a6a)"></div>
      <div class="dog-info" style="width:258px"><h4>Ruddyhound's Copper Trail JH (Copper)</h4><p>Reg #: RV315722094<br>Copper is out of our Hazel and Ridgeline Steadfast Ranger and is an excellent example of what a hunting dog should be. Copper earned her NFA Junior Hunting title.</p></div>
    </div>
    <div class="arrow" style="left:858px"><svg width="19" height="19"><path d="M12 4 6 9.5 12 15" fill="none" stroke="#8c6833" stroke-width="2"/></svg></div>
    <div class="arrow" style="left:888px"><svg width="19" height="19"><path d="M7 4 13 9.5 7 15" fill="none" stroke="#8c6833" stroke-width="2"/></svg></div>
  </section>

  <section class="abs info">
    <h3>For information and Queries, please contact us at</h3>
    <div class="info-row">
      <span><svg width="20" height="18" viewBox="0 0 20 18"><path d="M2 6c0-3 16-3 16 0v2h-4V6H6v2H2z" fill="#5a2f1c"/><path d="M5 9h10l3 8H2z" fill="#5a2f1c"/><circle cx="10" cy="13" r="2" fill="#fff"/></svg>515-555-0147</span>
      <span><svg width="20" height="16" viewBox="0 0 20 16"><rect x="0" y="1" width="20" height="14" fill="#5a2f1c"/><path d="M1 2l9 7 9-7" fill="none" stroke="#fff" stroke-width="1.5"/></svg>ruddyhound@mailpost.net</span>
    </div>
  </section>

  <footer class="abs footer">
    <span>Copyright © 2014 Ruddyhound Vizslas</span>
    <nav><span>Home</span><span>Our Dogs</span><span>Upcoming Litter</span><span>Contact Us</span><span>Photo Gallery</span><span>Past Litters</span></nav>
  </footer>
</div>
</body>
</html>
```